plumbers buisness card

A buisness card for a plumbing buisness
needs to have a water theme with navy blue, light blue and white
with an image of either a water drop, pipes, tools or something relating to plumbing and incorperating my buisness name as a logo

"Talcott Plumbing" is the words that need to stand out with "& gasfitting" to be smaller
Updates

spelling error on brief, "maintenance"
and also could you include my email m_talcott@nimbrel.com.au

Industry/Entity Type

Plumbing

Contact Information for Business Card

Talcott Plumbing & Gasfitting

myles talcott
0492315806

specialising in
-new homes
-maitenance
-renovations

license no.
-73846

```html
<!DOCTYPE html>
<html lang="en">
<head>
<meta charset="utf-8">
<title>Talcott Plumbing &amp; Gasfitting – Business Card</title>
<link href="https://fonts.googleapis.com/css2?family=Titillium+Web:wght@300;400;700;900&display=swap" rel="stylesheet">
<style>
  :root {
    --backdrop: #e9ecef;
    --card: #ffffff;
    --ink: #111111;
    --ink-soft: #3a3a3a;
    --ink-muted: #6b6b6b;
    --band-light: #cfe3f5;
    --band-mid: #6fb0e6;
    --band-deep: #2b7ccf;
    --steel-light: #eef1f4;
    --steel-dark: #b9c0c7;
  }
  * { box-sizing: border-box; margin: 0; padding: 0; }
  html, body { width: 1200px; height: 900px; overflow: hidden; }
  body {
    background: var(--backdrop);
    font-family: "Titillium Web", Arial, sans-serif;
    position: relative;
  }
  .card {
    position: absolute;
    left: 100px; top: 164px;
    width: 1000px; height: 572px;
    background: var(--card);
    border-radius: 6px;
    box-shadow: 0 14px 40px rgba(0,0,0,.18);
    overflow: hidden;
  }
  .brand {
    position: absolute; left: 60px; top: 40px;
    display: flex; align-items: flex-start; gap: 12px;
  }
  .brand-name {
    font-weight: 900; font-size: 76px; line-height: 1;
    color: var(--ink); letter-spacing: -1px;
  }
  .brand-trade {
    font-weight: 300; font-size: 34px; line-height: 0.95;
    color: var(--ink-soft); text-transform: uppercase; padding-top: 4px;
  }
  .licence {
    position: absolute; left: 500px; top: 122px;
    font-size: 15px; color: var(--ink-muted);
  }
  .plumbing-art {
    position: absolute; left: 60px; top: 168px;
    width: 250px; height: 262px; border-radius: 10px;
    background: linear-gradient(160deg, var(--steel-light) 0%, var(--steel-dark) 45%, var(--band-mid) 100%);
    opacity: .85;
  }
  .services {
    position: absolute; left: 330px; top: 215px;
    display: flex; gap: 24px; color: var(--ink-soft);
  }
  .services-title {
    font-weight: 400; font-size: 30px; text-transform: uppercase; letter-spacing: 1px;
    padding-top: 2px;
  }
  .services-list { list-style: none; }
  .services-list li {
    font-size: 32px; font-weight: 300; line-height: 1.25;
    display: flex; align-items: center; gap: 14px;
  }
  .services-list li::before {
    content: ""; width: 16px; height: 16px; border-radius: 50%;
    background: radial-gradient(circle, #fff 30%, var(--steel-dark) 34%);
    border: 1px solid #9aa2aa;
  }
  .contact {
    position: absolute; left: 560px; top: 360px; color: var(--ink-soft);
  }
  .contact-line { display: flex; align-items: center; gap: 12px; }
  .contact-phone { font-size: 36px; font-weight: 400; letter-spacing: 1px; line-height: 1.1; }
  .contact-email { font-size: 24px; font-weight: 300; }
  .contact-icon { width: 26px; height: 26px; flex: none; }
  .band {
    position: absolute; left: 0; right: 0; top: 460px; height: 82px;
    background: linear-gradient(90deg, var(--band-light) 0%, var(--band-mid) 45%, var(--band-deep) 100%);
    display: flex; align-items: center; padding-left: 330px;
  }
  .holder-name {
    font-size: 40px; font-weight: 300; color: var(--ink-soft); text-transform: capitalize;
  }
</style>
</head>
<body>
  <article class="card">
    <div class="plumbing-art" role="img" aria-label="Illustration of a chrome pipe with an elbow dripping a blue water drop"></div>

    <header class="brand">
      <span class="brand-name">Talcott Plumbing</span>
      <span class="brand-trade">&amp; Gas<br>Fitting</span>
    </header>
    <p class="licence">license no. 73846</p>

    <section class="services">
      <h2 class="services-title">Specialising in:</h2>
      <ul class="services-list">
        <li>New Homes</li>
        <li>Renovations</li>
        <li>Maintenance</li>
      </ul>
    </section>

    <section class="contact">
      <p class="contact-line contact-phone">
        <svg class="contact-icon" viewBox="0 0 26 26" aria-hidden="true">
          <circle cx="13" cy="13" r="12" fill="var(--band-deep)"/>
          <path d="M9 7c1 0 1.5 2.5 1.5 3s-1 1-1 1.5 2 4 4 4.5c.5 0 1-1 1.5-1s3 .5 3 1.5-1.5 2.5-2.5 2.5C11 19 7 14 7 9.5 7 8.5 8 7 9 7z" fill="#fff"/>
        </svg>
        049 231 5806
      </p>
      <p class="contact-line contact-email">
        <svg class="contact-icon" viewBox="0 0 26 26" aria-hidden="true">
          <circle cx="13" cy="13" r="12" fill="var(--band-deep)"/>
          <rect x="6.5" y="8.5" width="13" height="9" fill="none" stroke="#fff" stroke-width="1.5"/>
          <path d="M6.5 8.5 13 14l6.5-5.5" fill="none" stroke="#fff" stroke-width="1.5"/>
        </svg>
        m_talcott@nimbrel.com.au
      </p>
    </section>

    <footer class="band">
      <span class="holder-name">Myles Talcott</span>
    </footer>
  </article>
</body>
</html>
```